1 Home page redesign for existing repair service site.

We need a refresh of our existing website that looks more 2017. We have made a mockup of the content that we want and a sample of where we want it. Nothing is set in stone, if you have better ideas of where things should go, feel free.

You can see our current site at http://www.fixoloda.gr

The colors should stay orange/black/grey.

In many of the "boxes/banners" we will need images. Feel free to find in pixel vault as we have an account.

We have made notes throughout the wireframe that we have attached on what we are looking for. Let us know if you have any questions. Thanks.

Target Market(s)

People using technology and breaking it

Industry/Entity Type

It Service

Number of Pages Required

1 page

Font styles to use
Sans Serif

Requirements
Must have
• Must have a modern, professional look and feel. Need custom graphics and icons.

```html
<!DOCTYPE html>
<html lang="en">
<head>
<meta charset="utf-8">
<title>Fixoloda – Device Repairs</title>
<link rel="stylesheet" href="https://fonts.googleapis.com/css?family=Montserrat:400,600,700|Open+Sans:400,600,700&display=swap">
<style>
:root{
  --orange:#f26522;
  --dark:#222326;
  --darker:#151618;
  --grey:#e9e9ea;
  --mid:#8a8b8e;
  --text:#333;
  --line:#e1e1e1;
  --white:#fff;
}
*{box-sizing:border-box;margin:0;padding:0}
html,body{width:1200px;height:4110px;overflow:hidden}
body{font-family:"Open Sans",Arial,sans-serif;color:var(--text);background:var(--white);position:relative;font-size:14px}
.abs{position:absolute}
.ph{position:absolute;display:block}
/* top bar */
.topbar{position:absolute;top:0;left:0;width:1200px;height:33px;background:var(--darker)}
.topbar .quick{position:absolute;left:112px;top:7px;height:20px;padding:0 12px;border:1px solid #555;color:#ddd;font-size:10px;line-height:18px;letter-spacing:1px}
.topbar .social{position:absolute;left:825px;top:8px;display:flex;gap:5px}
.topbar .social span{width:17px;height:17px;border-radius:50%;background:#ddd;display:block}
.topbar .lang{position:absolute;left:965px;top:7px;height:20px;width:122px;border:1px solid #555;color:#ddd;font-size:10px;line-height:18px;text-align:center;letter-spacing:1px}
/* header */
.header{position:absolute;top:33px;left:0;width:1200px;height:77px;background:var(--white)}
.brand{position:absolute;left:112px;top:20px;display:flex;align-items:center;gap:10px;font-family:"Montserrat",sans-serif;font-weight:700;font-size:32px;color:var(--dark)}
.brand i{width:36px;height:36px;background:var(--orange);display:block;border-radius:4px}
.nav{position:absolute;left:475px;top:31px;display:flex;gap:26px;font-size:12px;font-weight:600;color:#444;letter-spacing:.5px}
.phone{position:absolute;left:748px;top:22px;display:flex;align-items:center;gap:10px;font-family:"Montserrat",sans-serif;font-size:21px;font-weight:700;color:var(--dark)}
.chat{position:absolute;left:960px;top:21px;display:flex;align-items:center;gap:10px;font-size:16px;font-weight:600;color:#333}
/* hero */
.hero{top:110px;left:0;width:1200px;height:487px;background:linear-gradient(180deg,#3a3b3e,#1c1d20 60%,#2b2a28)}
.hero .play{position:absolute;left:0;width:1200px;top:180px;text-align:center;color:#fff}
.hero .play b{font-family:"Montserrat",sans-serif;font-size:40px;font-weight:700;letter-spacing:2px;display:block;margin-top:12px}
.counter{position:absolute;top:597px;left:0;width:1200px;height:77px;background:var(--grey)}
.counter .digits{position:absolute;left:137px;top:12px;display:flex;gap:4px}
.counter .digits span{width:40px;height:54px;background:var(--dark);color:#fff;font-family:"Montserrat",sans-serif;font-size:34px;font-weight:700;text-align:center;line-height:54px;border-radius:3px}
.counter p{position:absolute;left:385px;top:26px;font-size:19px;color:#333;white-space:nowrap}
/* promo banners */
.promo{top:750px;height:302px;width:480px;overflow:hidden}
.promo .txt{position:absolute;left:210px;top:118px;color:#fff}
.promo small{font-size:10px;letter-spacing:1px;display:block;margin-bottom:6px}
.promo h3{font-family:"Montserrat",sans-serif;font-size:21px;line-height:26px;font-weight:700;text-transform:uppercase}
.promo p{font-size:12px;margin-top:6px;color:#ddd}
.promo a{color:var(--orange);font-size:14px;display:block;margin-top:8px;text-decoration:none}
/* feature cards */
.card{top:1126px;width:225px;height:367px;background:#efefef}
.card .img{height:212px}
.card h4{font-size:14px;font-weight:600;text-align:center;margin:22px 10px 0;color:#333;line-height:18px}
.card p{font-size:11.5px;text-align:center;color:#555;margin:8px 18px 0;line-height:15px}
.more{display:block;width:88px;height:28px;margin:14px auto 0;border:1.5px solid var(--orange);border-radius:14px;color:var(--orange);font-size:12px;text-align:center;line-height:25px}
/* section titles */
.stitle{position:absolute;left:0;width:1200px;text-align:center}
.stitle small{display:block;font-size:13px;letter-spacing:2px;color:#555}
.stitle h2{font-family:"Montserrat",sans-serif;font-weight:400;font-size:26px;letter-spacing:2px;color:#333;text-transform:uppercase;margin-top:2px}
.stitle i{display:block;width:36px;height:2px;background:var(--orange);margin:10px auto 0;position:relative}
.stitle i:after{content:"";position:absolute;left:14px;top:-3px;width:8px;height:8px;background:var(--orange);border-radius:50%}
/* services */
.svc{width:300px;height:132px;border:1px solid var(--line);background:#fff}
.svc svg{position:absolute;left:-14px;top:40px;background:#fff}
.svc h5{position:absolute;left:42px;top:18px;font-size:15px;font-weight:600;color:#333}
.svc p{position:absolute;left:42px;top:46px;width:236px;font-size:11.5px;line-height:16px;color:#666}
.svc.on{background:var(--orange);border-color:var(--orange)}
.svc.on h5,.svc.on p{color:#fff}
/* repair options */
.options{top:2343px;height:74px;display:flex}
.opt{position:relative;height:74px;display:flex;align-items:center;color:#fff;padding-left:40px;gap:14px}
.opt b{font-family:"Montserrat",sans-serif;font-size:22px;font-weight:700;letter-spacing:1px;display:block;line-height:24px}
.opt span{font-size:12px}
/* why choose */
.why{top:2614px;width:310px;height:252px}
.whycap{top:2882px;width:310px;text-align:center;font-size:15px;color:#333}
/* testimonials */
.quote{top:3104px;width:240px;height:156px;border:1px solid var(--line);padding:16px 18px;font-size:11.5px;line-height:16px;color:#555}
.quote em{font-style:normal;color:var(--orange);display:block;margin-top:8px}
.quote .tick{display:flex;gap:6px;align-items:center;margin-top:2px;color:#444}
.rev{top:3270px;width:240px;display:flex;align-items:center;gap:10px}
.rev .av{width:40px;height:40px;border-radius:50%;background:#c69a7d}
.rev .stars{color:var(--orange);font-size:19px;letter-spacing:2px;line-height:20px}
.rev small{font-size:11px;color:#444;display:block;text-align:center;margin-left:-30px}
/* footer */
.footer{top:3425px;left:0;width:1200px;height:350px;background:linear-gradient(180deg,#2b2c2f,#1d1e20)}
.footer h6{font-size:15px;font-weight:700;color:#fff}
.field{width:390px;height:42px;background:#fff;font-size:11px;color:#999;padding:14px 12px}
.send{width:140px;height:40px;background:var(--orange);color:#fff;font-weight:700;font-size:13px;text-align:center;line-height:40px;letter-spacing:2px}
.blog{left:530px;width:330px;height:278px;background:rgba(90,90,92,.55);padding:22px 26px}
.blog h6{font-family:"Montserrat",sans-serif;font-size:24px;font-weight:400;letter-spacing:1px}
.post{display:flex;gap:14px;margin-top:20px}
.post .dot{flex:none;width:46px;height:46px;border-radius:50%}
.post p{font-size:11.5px;line-height:16px;color:#eee}
.post small{color:var(--orange);font-size:10px}
.links li{list-style:none;font-size:12px;color:#eee;line-height:27px}
/* contact */
.contact{top:3932px;width:320px;display:flex;gap:14px}
.contact b{font-size:20px;font-weight:600;color:#333;display:block;line-height:24px}
.contact span{font-size:12px;color:#444;display:block}
.contact a{font-size:13px;color:var(--orange);text-decoration:none;display:block;margin-top:3px}
.bottom{top:4055px;left:0;width:1200px;height:55px;background:var(--darker)}
.bottom .cards{position:absolute;left:112px;top:17px;display:flex;gap:6px}
.bottom .cards span{width:40px;height:24px;background:#eee;border-radius:2px;display:block}
.bottom p{position:absolute;right:112px;top:18px;color:#ccc;font-size:12px}
</style>
</head>
<body>

<div class="topbar">
  <div class="quick">QUICK LINKS ▾</div>
  <div class="social"><span></span><span></span><span></span><span></span><span></span><span></span></div>
  <div class="lang">■ ENGLISH ▾</div>
</div>

<header class="header">
  <div class="brand"><i></i>Fixoloda</div>
  <nav class="nav"><span>REPAIRS ▾</span><span>20 STORES ▾</span><span>BLOG</span></nav>
  <div class="phone"><svg width="18" height="34" viewBox="0 0 18 34"><rect x="1" y="1" width="16" height="32" rx="3" fill="none" stroke="#222" stroke-width="2.5"/><circle cx="9" cy="28" r="1.8" fill="#222"/></svg>210 555 0142</div>
  <div class="chat"><svg width="38" height="36" viewBox="0 0 38 36"><path d="M19 2C9 2 2 8 2 16c0 5 3 9 7 11l-2 7 8-5c1 0 3 1 4 1 10 0 17-6 17-14S29 2 19 2z" fill="#333"/><circle cx="12" cy="16" r="2" fill="#fff"/><circle cx="19" cy="16" r="2" fill="#fff"/><circle cx="26" cy="16" r="2" fill="#fff"/></svg>Live Chat</div>
</header>

<section class="ph hero" role="img" aria-label="Photo of technicians working at a busy repair store counter">
  <div class="play">
    <svg width="64" height="64" viewBox="0 0 64 64"><circle cx="32" cy="32" r="31" fill="#fff"/><path d="M26 19l19 13-19 13z" fill="#222"/></svg>
    <b>PLAY VIDEO</b>
  </div>
</section>

<section class="counter">
  <div class="digits"><span>3</span><span>2</span><span>5</span><span>4</span><span>7</span></div>
  <p>Repairs Completed with Happy Customers. Yep, We Fix a Lot of Devices!</p>
</section>

<section class="ph promo" style="left:112px;background:linear-gradient(135deg,#c9c9c9,#555 55%,#2a2a2a)" role="img" aria-label="Hand holding a phone showing a store locator map">
  <div class="txt" style="left:215px;text-align:right;width:245px"><small>LOREM IPSUM DOLOR SIT</small><h3>20 Fixoloda locations find a store near you</h3><a>View Map →</a></div>
</section>
<section class="ph promo" style="left:605px;background:linear-gradient(135deg,#6a6a6a,#2a2a2a 50%,#9a9a9a)" role="img" aria-label="Technician repairing the inside of a desktop computer">
  <div class="txt" style="left:28px;top:106px;width:260px"><small>LOW PRICE GUARANTEE</small><h3>Vantelis price guarantee</h3><p>Find a lower price for your phone or tablet repair? We will match it!</p></div>
</section>

<article class="ph card" style="left:112px"><div class="img" style="background:linear-gradient(135deg,#a9c3d6,#d9d2b8)" role="img" aria-label="Map of store locations"></div><h4>Open Service Area</h4><p>Repairs Right in Front of you No Closed Doors</p><span class="more">MORE</span></article>
<article class="ph card" style="left:362px"><div class="img" style="background:linear-gradient(135deg,#e4e4e4,#8d8d8d)" role="img" aria-label="Tablet with a cracked screen"></div><h4>Save 50-75% on Multiple Repairs</h4><p>If your device needs more save up to 75% on addition parts.</p><span class="more">MORE</span></article>
<article class="ph card" style="left:614px;background:linear-gradient(180deg,#7a7a7c,#3c3d40)" role="img" aria-label="Staff member holding a laptop">
  <h4 style="position:absolute;top:240px;width:100%;color:#fff;margin:0">Accessories</h4>
  <div style="position:absolute;top:275px;width:100%;display:flex;justify-content:center;gap:6px"><span style="width:8px;height:8px;border-radius:50%;background:#fff"></span><span style="width:8px;height:8px;border-radius:50%;background:var(--orange)"></span><span style="width:8px;height:8px;border-radius:50%;background:#fff"></span><span style="width:8px;height:8px;border-radius:50%;background:#fff"></span></div>
</article>
<article class="ph card" style="left:863px"><div class="img" style="background:linear-gradient(135deg,#cfd4da,#6b727a)" role="img" aria-label="Phone parts on a repair bench"></div><h4>Minute Repairs 20</h4><p>Most repairs can be completed in about 20 minutes.</p><span class="more">MORE</span></article>

<div class="stitle" style="top:1567px"><small>WHAT WE REPAIR</small><h2>Business Services</h2><i></i></div>

<div class="ph svc on" style="left:142px;top:1677px"><svg width="30" height="52" viewBox="0 0 30 52"><rect x="7" y="10" width="16" height="30" rx="3" fill="none" stroke="#f26522" stroke-width="2"/></svg><h5>Novaphone Repair</h5><p>Lorem ipsum dolor sit amet, consectetur adipiscing elit, sed do eiusmod tempor incididunt ut</p></div>
<div class="ph svc" style="left:475px;top:1677px"><svg width="30" height="52" viewBox="0 0 30 52"><rect x="5" y="8" width="20" height="34" rx="3" fill="none" stroke="#f26522" stroke-width="2"/></svg><h5>Novatab Repair</h5><p>Lorem ipsum dolor sit amet, consectetur adipiscing elit, sed do eiusmod tempor incididunt ut</p></div>
<div class="ph svc" style="left:788px;top:1677px"><svg width="30" height="52" viewBox="0 0 30 52"><rect x="8" y="10" width="14" height="30" rx="3" fill="none" stroke="#f26522" stroke-width="2"/></svg><h5>Novaplay Touch Repair</h5><p>Lorem ipsum dolor sit amet, consectetur adipiscing elit, sed do eiusmod tempor incididunt ut</p></div>

<div class="ph svc" style="left:142px;top:1852px"><svg width="30" height="52" viewBox="0 0 30 52"><rect x="7" y="10" width="16" height="30" rx="3" fill="none" stroke="#f26522" stroke-width="2"/></svg><h5>Korvex Repair</h5><p>Lorem ipsum dolor sit amet, consectetur adipiscing elit, sed do eiusmod tempor incididunt ut</p></div>
<div class="ph svc" style="left:475px;top:1852px"><svg width="30" height="52" viewBox="0 0 30 52"><rect x="7" y="10" width="16" height="30" rx="2" fill="none" stroke="#f26522" stroke-width="2"/><line x1="7" y1="26" x2="23" y2="26" stroke="#f26522" stroke-width="2"/></svg><h5>Duskline Repair</h5><p>Lorem ipsum dolor sit amet, consectetur adipiscing elit, sed do eiusmod tempor incididunt ut</p></div>
<div class="ph svc" style="left:788px;top:1852px"><svg width="30" height="52" viewBox="0 0 30 52"><rect x="2" y="12" width="26" height="20" rx="2" fill="none" stroke="#f26522" stroke-width="2"/><path d="M11 40h8M15 32v8" stroke="#f26522" stroke-width="2"/></svg><h5>Novadesk Repairs</h5><p>Lorem ipsum dolor sit amet, consectetur adipiscing elit, sed do eiusmod tempor incididunt ut</p></div>

<div class="ph svc" style="left:142px;top:2028px"><svg width="30" height="52" viewBox="0 0 30 52"><rect x="5" y="14" width="20" height="16" rx="1" fill="none" stroke="#f26522" stroke-width="2"/><path d="M1 34h28" stroke="#f26522" stroke-width="2"/></svg><h5>Novabook Repair</h5><p>Lorem ipsum dolor sit amet, consectetur adipiscing elit, sed do eiusmod tempor incididunt ut</p></div>
<div class="ph svc" style="left:475px;top:2028px"><svg width="30" height="52" viewBox="0 0 30 52"><rect x="2" y="12" width="22" height="18" rx="1" fill="none" stroke="#f26522" stroke-width="2"/><rect x="20" y="16" width="8" height="22" fill="#fff" stroke="#f26522" stroke-width="2"/><path d="M9 38h8" stroke="#f26522" stroke-width="2"/></svg><h5>Computer Repair</h5><p>Lorem ipsum dolor sit amet, consectetur adipiscing elit, sed do eiusmod tempor incididunt ut</p></div>
<div class="ph svc" style="left:788px;top:2028px"><svg width="30" height="52" viewBox="0 0 30 52"><rect x="5" y="14" width="20" height="16" rx="1" fill="none" stroke="#f26522" stroke-width="2"/><path d="M1 34h28" stroke="#f26522" stroke-width="2"/></svg><h5>Laptop Repair</h5><p>Lorem ipsum dolor sit amet, consectetur adipiscing elit, sed do eiusmod tempor incididunt ut</p></div>

<div class="stitle" style="top:2241px"><small>REPAIR</small><h2>Options</h2><i></i></div>

<div class="ph options" style="left:112px;width:976px">
  <svg class="abs" style="left:0;top:0" width="976" height="74" viewBox="0 0 976 74">
    <polygon points="0,0 320,0 345,37 320,74 0,74" fill="#2a2b2e"/>
    <polygon points="320,0 640,0 665,37 640,74 320,74 345,37" fill="#f26522"/>
    <polygon points="640,0 976,0 976,74 640,74 665,37" fill="#2a2b2e"/>
  </svg>
  <div class="opt" style="width:330px;padding-left:36px"><svg width="40" height="28" viewBox="0 0 40 28"><rect x="1" y="4" width="22" height="16" fill="#fff"/><path d="M23 9h9l6 6v5H23z" fill="#fff"/><circle cx="9" cy="22" r="4" fill="#fff" stroke="#2a2b2e" stroke-width="2"/><circle cx="31" cy="22" r="4" fill="#fff" stroke="#2a2b2e" stroke-width="2"/></svg><div><b>FIND A STORE</b><span>Near You</span></div></div>
  <div class="opt" style="width:320px;padding-left:50px"><svg width="34" height="34" viewBox="0 0 34 34"><circle cx="17" cy="17" r="16" fill="#fff"/><text x="17" y="23" text-anchor="middle" font-size="16" font-weight="700" fill="#f26522" font-family="Arial,sans-serif">%</text></svg><div><b>SEND US YOUR</b><span>Device</span></div></div>
  <div class="opt" style="width:326px;padding-left:52px"><svg width="36" height="30" viewBox="0 0 36 30"><path d="M2 4h18l14 11-14 11H2z" fill="#fff" transform="rotate(-20 18 15)"/><circle cx="9" cy="13" r="3" fill="#2a2b2e"/></svg><div><b>FREE PICKUP</b><span>In Athens</span></div></div>
</div>

<div class="stitle" style="top:2505px"><small>WHY</small><h2>Choose Fixoloda</h2><i></i></div>
<div class="ph why" style="left:112px;background:linear-gradient(135deg,#dfe6ee,#7b8794)" role="img" aria-label="Laptop on a desk showing the store website"></div>
<div class="ph why" style="left:445px;background:linear-gradient(135deg,#8a7766,#3b342f)" role="img" aria-label="Hands repairing a computer circuit board"></div>
<div class="ph why" style="left:778px;background:linear-gradient(135deg,#e8e8e8,#9a9a9a)" role="img" aria-label="Customer handing a laptop to a technician"></div>
<div class="ph whycap" style="left:112px">Open Service Area</div>
<div class="ph whycap" style="left:445px">Accessories</div>
<div class="ph whycap" style="left:778px">Minute Repairs 20</div>
<svg class="abs" style="left:72px;top:2725px" width="30" height="30" viewBox="0 0 30 30"><circle cx="15" cy="15" r="15" fill="#bbb"/><path d="M17 9l-6 6 6 6" stroke="#fff" stroke-width="2.5" fill="none"/></svg>
<svg class="abs" style="left:1096px;top:2725px" width="30" height="30" viewBox="0 0 30 30"><circle cx="15" cy="15" r="15" fill="#f26522"/><path d="M13 9l6 6-6 6" stroke="#fff" stroke-width="2.5" fill="none"/></svg>

<div class="stitle" style="top:2987px"><small>WHAT OUR</small><h2>Customers Say</h2><i></i></div>
<svg class="abs" style="left:152px;top:3170px" width="16" height="28" viewBox="0 0 16 28"><path d="M13 2L3 14l10 12" stroke="#bbb" stroke-width="3" fill="none"/></svg>
<svg class="abs" style="left:1030px;top:3170px" width="16" height="28" viewBox="0 0 16 28"><path d="M3 2l10 12-10 12" stroke="#f26522" stroke-width="3" fill="none"/></svg>

<div class="ph quote" style="left:200px">Lorem ipsum dolor sit amet,con sectetur adipisicing elit, sed do eiu smod tempor incididunt..<em>Laptop Repair</em><div class="tick"><svg width="12" height="10" viewBox="0 0 12 10"><path d="M1 5l3 3 7-7" stroke="#f26522" stroke-width="2" fill="none"/></svg>Overheating</div></div>
<div class="ph quote" style="left:478px">Lorem ipsum dolor sit amet,con sectetur adipisicing elit, sed do eiu smod tempor incididunt..<em>Novaphone 6 Repair</em><div class="tick"><svg width="12" height="10" viewBox="0 0 12 10"><path d="M1 5l3 3 7-7" stroke="#f26522" stroke-width="2" fill="none"/></svg>Screen Replacement</div></div>
<div class="ph quote" style="left:755px">Lorem ipsum dolor sit amet,con sectetur adipisicing elit, sed do eiu smod tempor incididunt..<em>Novaphone 7 Repair</em><div class="tick"><svg width="12" height="10" viewBox="0 0 12 10"><path d="M1 5l3 3 7-7" stroke="#f26522" stroke-width="2" fill="none"/></svg>Screen Replacement</div></div>

<div class="ph rev" style="left:215px"><div class="av" role="img" aria-label="Customer portrait"></div><div><div class="stars">★★★★★</div><small>Eleni M Kifisia</small></div></div>
<div class="ph rev" style="left:490px"><div class="av" style="background:#8e6a55" role="img" aria-label="Customer portrait"></div><div><div class="stars">★★★★★</div><small>Petros A. Larissa</small></div></div>
<div class="ph rev" style="left:768px"><div class="av" style="background:#a88a78" role="img" aria-label="Customer portrait"></div><div><div class="stars">★★★★★</div><small>Sofia D. Patra</small></div></div>

<footer class="ph footer">
  <h6 class="abs" style="left:112px;top:62px">Sign up for Our Newsletter</h6>
  <div class="ph field" style="left:112px;top:100px">Your Name</div>
  <div class="ph field" style="left:112px;top:155px">Your Email</div>
  <div class="ph send" style="left:112px;top:210px">SEND</div>
  <div class="abs" style="left:883px;top:56px"><h6>Quick Links</h6>
    <ul class="links" style="margin-top:8px"><li>About Fixoloda</li><li>Business Services</li><li>Schedule a pickup</li><li>Job Openings</li><li>Shipping Instructions</li><li>Privacy Policy</li><li>Send your Device with QuickPoint</li></ul>
  </div>
</footer>
<div class="ph blog" style="top:3450px"><h6 style="color:#fff">FIXOLODA BLOG</h6>
  <div class="post"><span class="dot" style="background:#2aa7e0"></span><div><p>These are the 3 Simple but important steps to look after our PC,</p><small>March 08, 2017</small></div></div>
  <div class="post"><span class="dot" style="background:#e2244e"></span><div><p>These are the 3 Simple but important steps to look after our PC,</p><small>March 03, 2017</small></div></div>
</div>

<div class="stitle" style="top:3822px"><small>CAN'T FIND</small><h2>What You Need</h2><i></i></div>

<div class="ph contact" style="left:112px"><svg width="40" height="30" viewBox="0 0 40 30"><rect x="1" y="1" width="38" height="28" fill="none" stroke="#f26522" stroke-width="2"/><path d="M1 1l19 15L39 1" stroke="#f26522" stroke-width="2" fill="none"/></svg><div><b>Email Support</b><span>We Usually Respond Within 24 Hours</span><a>Click to Send Email</a></div></div>
<div class="ph contact" style="left:470px"><svg width="36" height="40" viewBox="0 0 36 40"><circle cx="18" cy="12" r="9" fill="none" stroke="#f26522" stroke-width="2"/><path d="M3 39c1-10 7-15 15-15s14 5 15 15" fill="none" stroke="#f26522" stroke-width="2"/><path d="M7 12a11 11 0 0 1 22 0" fill="none" stroke="#f26522" stroke-width="3"/></svg><div><b>Contact our Call Center</b><span>Call to Speak to a Customer Service Rep.</span><a>210 555 0142</a></div></div>
<div class="ph contact" style="left:820px"><svg width="38" height="34" viewBox="0 0 38 34"><path d="M3 3h26v18H13l-7 6v-6H3z" fill="none" stroke="#f26522" stroke-width="2"/><path d="M32 10h4v16h-3v5l-6-5H16" fill="none" stroke="#f26522" stroke-width="2"/></svg><div><b>Live Chat</b><span>Chat with a Fixoloda Technician Now</span><a>Click to Chat</a></div></div>

<div class="ph bottom">
  <div class="cards"><span></span><span></span><span></span><span></span></div>
  <p>© Fixoloda 2017 | Bright Grid Studio</p>
</div>

</body>
</html>
```